Real Estate 24"x24" Sign, Business Card, Letter Head and Envelope

This is a 4 project contest. If we choose a design or designs we like from what you sent we are willing to pay an amount at our discretion for that design even if we don't like all your designs for the 4 projects. Please be creative. Attached are our logo files. Please message us with any questions. Thanks and Good Luck!
Project 1: QMTD Realty 24" x 24" yard sign
We want to use the same blue background in our logo for the sign where the logo in white font will be on. CMYK 100,80,0,0. Attached is a sample a local designer made for you to get an idea what we are looking for. In the sample, the website is way too big and the entire sign is very plain and not attractive looking plus blue color is wrong one. We want the logo on top as large as possible but keeping it proportionate and attractive looking buy not too big that it looks odd. The following information can go in white color background or same blue color background color. Our company colors are blue (as per logo), green (as per logo), and white. "Residential & Commercial" goes under the logo. Under that put our phone number "312-640-5918" as large as possible but still looks good and under that our website in much smaller but readable font "www.qmtdrealty.com".
Project 2: Envelope
We have two version of the logo. Use one or both. Whatever looks best in your design. The envelope will be white. We only want on top left corner logo and underneath our mailing address: 5147 Hawthorne Ave. Skokie, IL 60091-2714. Maybe some creative decorative design at bottom of envelope will look nice
Project 3: Letter Head
We have two version of the logo. Use one or both. Whatever looks best in your design. We want the following information on the top of the letterhead. Logo, address: 5147 Hawthorne Ave., Skokie, IL 60091-2714, phone: 312-640-5918, fax: 312-918-6057 website www.qmtdrealty.com, email: info@qmtdrealty.com
Project 4: Business card
Use either logo. We need cards for two individuals. Information for Person 1: Dev Mehta, Managing Broker, Phone: 312-640-5918, Email: dev.mehta@qmtdrealty.com. Person 2: Raj Mehta Broker Phone: 312-285-3390 Email: raj.mehta@qmtdrealty.com. Add Address, Fax and website same as above letter head.

```html
<!DOCTYPE html>
<html lang="en">
<head>
<meta charset="utf-8">
<title>QMTD Realty Yard Sign</title>
<link rel="stylesheet" href="https://fonts.googleapis.com/css2?family=Roboto+Condensed:wght@700&family=Roboto:wght@700&display=swap">
<style>
  :root {
    --brand-blue: #0b4aa2;
    --brand-blue-text: #0d4ea6;
    --brand-green: #6abf45;
    --white: #ffffff;
    --stage: #1d1d1f;
  }
  html, body {
    margin: 0;
    padding: 0;
    width: 1200px;
    height: 999px;
    overflow: hidden;
    background: var(--stage);
  }
  .yard-sign {
    position: absolute;
    left: 240px;
    top: 140px;
    width: 720px;
    height: 718px;
    overflow: hidden;
  }
  .sign-background {
    position: absolute;
    inset: 0;
    width: 720px;
    height: 718px;
  }
  .brand-name {
    position: absolute;
    left: 0;
    right: 0;
    top: 150px;
    margin: 0;
    text-align: center;
    font-family: "Roboto Condensed", sans-serif;
    font-weight: 700;
    font-size: 104px;
    line-height: 1;
    color: var(--white);
    white-space: nowrap;
  }
  .service-line {
    position: absolute;
    left: 70px;
    width: 610px;
    top: 396px;
    margin: 0;
    text-align: center;
    font-family: "Roboto Condensed", sans-serif;
    font-weight: 700;
    font-size: 51px;
    line-height: 1;
    color: var(--white);
    white-space: nowrap;
  }
  .phone-number {
    position: absolute;
    left: 0;
    right: 0;
    top: 540px;
    margin: 0;
    text-align: center;
    font-family: "Roboto Condensed", sans-serif;
    font-weight: 700;
    font-size: 104px;
    line-height: 1;
    color: var(--brand-blue-text);
    white-space: nowrap;
  }
  .website {
    position: absolute;
    left: 0;
    right: 0;
    top: 650px;
    margin: 0;
    text-align: center;
    font-family: "Roboto", sans-serif;
    font-weight: 700;
    font-size: 40px;
    line-height: 1;
    color: var(--brand-blue-text);
    white-space: nowrap;
  }
</style>
</head>
<body>
  <section class="yard-sign">
    <svg class="sign-background" viewBox="0 0 720 718" aria-hidden="true">
      <rect class="blue-field" width="720" height="718" fill="var(--brand-blue)"/>
      <path class="green-swoosh" d="M150,528 Q430,530 720,448 L720,482 Q420,556 150,528 Z" fill="var(--brand-green)"/>
      <path class="white-field" d="M0,506 Q330,550 720,480 L720,718 L0,718 Z" fill="var(--white)"/>
    </svg>
    <h1 class="brand-name">QMTD Realty</h1>
    <p class="service-line">Residential &amp; Commercial</p>
    <p class="phone-number">312-640-5918</p>
    <p class="website">QMTDrealty.com</p>
  </section>
</body>
</html>
```